KAZ Freightworks #ALLKAZ Business Cards & Letterhead

I am looking to business cards designed for our organization. We are currently undergoing a small re-branding that is taking place. Our organization is called KAZ Freightworks and we are headquartered in Phoenix, AZ. We primarily provide transportation and logistics services to the Meridel Parcel Bureau who is our largest customer. I would like to see a design that incorporates name, title, contact info, website, and address (this will be different depending on the employee). I would also like to see some color on the business card using our logo colors or a variation. I would like our logo on the back of the business card with the website displayed. The final design should communicate that we are a next generation transportation operate that focuses on being driver-first, customer-centric, innovative, and sustainable.We would also like our #ALLKAZ catch phrase incorporated as well.
Updates

Decision maker traveling outside of the country until Monday, November 25th.

Target Market(s)

Transportation & Logistics

Industry/Entity Type

Trucking Company

Contact Information for Business Card

-First and Last Name
-Position Title
-Contact Phone
-Contact Email
-Physical Address

Font styles to use
Serif

Colors

Designer to choose colors to be used in the design.

Requirements
Must have
• -KAZ logo prominently displayed
• -#ALLKAZ catch phrase used
• -Some amount of color, design gradient, etc.
• -Logo on the back with website listed (https://www.kazfreightco.example)

```html
<!DOCTYPE html>
<html lang="en">
<head>
<meta charset="utf-8">
<title>KAZ Freightworks Business Card</title>
<link rel="stylesheet" href="https://fonts.googleapis.com/css2?family=Roboto+Slab:wght@400;500;600;800&display=swap">
<style>
  :root {
    --teal: #0f3947;
    --green: #82c341;
    --white: #ffffff;
    --backdrop: #262626;
  }
  * { margin: 0; padding: 0; box-sizing: border-box; }
  html, body { width: 1200px; height: 900px; overflow: hidden; }
  body {
    background: var(--backdrop);
    font-family: "Roboto Slab", serif;
    position: relative;
  }
  .card {
    position: absolute;
    left: 261px;
    width: 656px;
    height: 357px;
    border-radius: 26px;
    overflow: hidden;
  }
  .card-front { top: 69px; background: var(--white); color: var(--teal); }
  .card-back { top: 472px; background: var(--teal); color: var(--white); }

  .front-art, .back-art { position: absolute; inset: 0; }

  .name-accent {
    position: absolute; left: 0; top: 66px;
    width: 11px; height: 41px; background: var(--teal);
  }
  .person-name {
    position: absolute; left: 27px; top: 64px;
    font-size: 25px; font-weight: 500; letter-spacing: 0.6px;
    color: var(--green); line-height: 1;
  }
  .person-title {
    position: absolute; left: 27px; top: 93px;
    font-size: 17px; font-weight: 400; letter-spacing: 0.4px; line-height: 1;
  }
  .address {
    position: absolute; left: 27px; top: 143px;
    font-size: 16px; letter-spacing: 0.3px; line-height: 22.5px;
    font-style: normal;
  }
  .contact-list {
    position: absolute; left: 27px; top: 233px;
    list-style: none;
    font-size: 16px; letter-spacing: 0.2px; line-height: 22.3px;
  }
  .contact-list li { display: flex; align-items: center; }
  .contact-icon { width: 11px; height: 11px; margin-right: 8px; flex: none; }
  .accent-text { color: var(--green); }

  .catch-phrase {
    position: absolute; left: 0; right: 0; top: 281px;
    text-align: center; font-size: 15px; font-weight: 600;
    letter-spacing: 3px; line-height: 1; color: var(--green);
  }
  .back-website {
    position: absolute; left: 0; right: 0; top: 318px;
    text-align: center; font-size: 16px; font-weight: 500;
    letter-spacing: 2.5px; line-height: 1;
  }
</style>
</head>
<body>

<section class="card card-front" aria-label="Business card front">
  <svg class="front-art" width="656" height="357" viewBox="0 0 656 357">
    <rect class="brand-panel" x="469" y="0" width="187" height="357" fill="var(--green)"/>
    <circle class="panel-cutout" cx="469" cy="178" r="158" fill="var(--white)"/>
    <circle class="brand-ring" cx="469" cy="178" r="140" fill="none" stroke="var(--green)" stroke-width="10"/>
    <text class="brand-name" x="469" y="214" text-anchor="middle"
          font-family="'Roboto Slab', serif" font-weight="800" font-size="98"
          fill="var(--teal)">KAZ</text>
  </svg>

  <span class="name-accent"></span>
  <h1 class="person-name">DARREN HOLLIS</h1>
  <p class="person-title">Director</p>

  <address class="address">
    4170 North Cactus<br>
    Ridge Boulevard<br>
    Glendale, AZ 85308
  </address>

  <ul class="contact-list">
    <li>
      <svg class="contact-icon" viewBox="0 0 12 12" aria-hidden="true">
        <path d="M3 1 L5 3.5 L4 5 Q5 7.5 7 8 L8.5 7 L11 9 L9.5 11 Q3 10 1 2.5 Z" fill="none" stroke="var(--green)" stroke-width="1.2"/>
      </svg>
      623-555-0148
    </li>
    <li>
      <svg class="contact-icon" viewBox="0 0 12 12" aria-hidden="true">
        <rect x="1" y="2.5" width="10" height="7" fill="none" stroke="var(--green)" stroke-width="1.2"/>
        <path d="M1 2.5 L6 6.5 L11 2.5" fill="none" stroke="var(--green)" stroke-width="1.2"/>
      </svg>
      info@kazfreightco.example
    </li>
    <li>
      <svg class="contact-icon" viewBox="0 0 12 12" aria-hidden="true">
        <circle cx="6" cy="6" r="5" fill="none" stroke="var(--green)" stroke-width="1"/>
        <ellipse cx="6" cy="6" rx="2.2" ry="5" fill="none" stroke="var(--green)" stroke-width="1"/>
        <path d="M1 6 H11 M2 3.5 H10 M2 8.5 H10" stroke="var(--green)" stroke-width="1"/>
      </svg>
      www.<span class="accent-text">kazfreightco</span>.example
    </li>
  </ul>
</section>

<section class="card card-back" aria-label="Business card back">
  <svg class="back-art" width="656" height="357" viewBox="0 0 656 357">
    <circle class="brand-ring" cx="328" cy="172" r="87" fill="none" stroke="var(--green)" stroke-width="6"/>
    <text class="brand-name" x="328" y="195" text-anchor="middle"
          font-family="'Roboto Slab', serif" font-weight="800" font-size="62"
          fill="var(--white)">KAZ</text>
  </svg>
  <p class="catch-phrase">#ALLKAZ</p>
  <p class="back-website">www.kazfreightco.example</p>
</section>

</body>
</html>
```